World Class Resort Requires Design for Marketing and Large Road Signage Purposes

We want a design that will take us to a new level, you can visit our web address to see the property details, www.brookmerefields.com we want the design to be full of colour, character, and a real one off it must attract customers including children to visit our resort / adventure park. we require the following features etc in the design by way of design not words - Golf Course - Mini Golf 18 holes - Jumping Pillow - Pedal Bikes - Water Bubbles - Lakeside Dining - Resort Accommodation - Swiss Shopping Village - Ice Cream Shop - Bakery - Wedding Chapel - Conferences - Hillside Look out - Numerous Lakes with Ducks trees and trout fish - Mountain Streams - Lakeside Villas.

The resort is built around a Swiss style theme buildings and is located in one of the most exotic - green, leafy, grassy areas of the World - The main design focus is to be on HOLLENBERG.COM.AU , the design must say 10 minutes drive North of Launceston

The design will be used on large 6 metre - 4 metre billboards around the State of Tasmania Australia
Updates

Hello,  We have just posted a number of images of the property and its features - we would like to follow the animated type Pemberly theme or similar as also posted on the brief  Please advise if you need anything extra  Thanks Ray  RAY@PK.COM.AU

The uploaded file number 4 of Wonderpark is the similar theme we would like created = all other images posted are of our property features Thanks Ray

Reason: Date has been extended as designer have requested some extra time to submit their designs Thanks

Reason: Designers have asked for additional time

Target Market(s)

Families, Weddings, Conferences, Holiday Makers, Day Visitors - Please look at the image we have uploaded as a similar format if possible. Thanks Ray

Industry/Entity Type

Accommodation

Font styles to use
Decorative

Requirements
Must have
• we require the following features etc in the design by way of design not words - Golf Course - Mini Golf 18 holes - Jumping Pillow - Pedal Bikes - Water Bubbles - Lakeside Dining - Resort Accommodation - Swiss Shopping Village - Ice Cream Shop - Bakery - Wedding Chapel - Conferences - Hillside Look out - Numerous Lakes with Ducks trees and trout fish - Mountain Streams - Lakeside Villas.
Must have an exotic - green, leafy, Hillside stream, lake, grassy appeal and be fun and exciting as well
The main design focus is to be on HOLLENBERG.COM.AU , the design must say 10 minutes drive North of Launceston
Should not have
• Dark Colours, dreary design, to much text

```html
<!DOCTYPE html>
<html lang="en">
<head>
<meta charset="utf-8">
<title>Brookmere Fields – Road Billboard</title>
<link rel="stylesheet" href="https://fonts.googleapis.com/css2?family=Archivo:wght@400;900&display=swap">
<style>
  :root {
    --page-bg: #e9ecea;
    --green-deep: #1f7a1a;
    --green-main: #2f9a22;
    --green-bright: #5fd43a;
    --swoosh-white: #f4f4f4;
    --swoosh-grey: #c9cbcb;
    --ring-dark: #4a4d4f;
    --text-dark: #163d12;
    --text-light: #ffffff;
  }
  * { margin: 0; padding: 0; box-sizing: border-box; }
  html, body {
    width: 1200px;
    height: 800px;
    overflow: hidden;
    background: var(--page-bg);
  }
  .canvas {
    position: relative;
    width: 1200px;
    height: 800px;
  }
  .billboard {
    position: absolute;
    left: 50px;
    top: 150px;
    width: 1100px;
    height: 500px;
    box-shadow: 0 6px 18px rgba(0,0,0,0.25);
  }
  .billboard svg { display: block; }
  .tagline {
    font-family: "Archivo", Arial, sans-serif;
    fill: var(--text-dark);
  }
  .tagline .strong { font-weight: 900; }
  .tagline .light { font-weight: 400; }
  .brand-name {
    font-family: "Archivo", Arial, sans-serif;
    font-weight: 900;
    fill: var(--text-light);
    font-size: 52px;
    letter-spacing: 2px;
  }
  .brand-url {
    font-family: "Archivo", Arial, sans-serif;
    font-weight: 400;
    fill: var(--text-light);
    font-size: 17px;
  }
  .feature-ring { fill: none; stroke: var(--ring-dark); stroke-width: 7; }
</style>
</head>
<body>
<div class="canvas">
  <div class="billboard">
    <svg width="1100" height="500" viewBox="0 0 1100 500" xmlns="http://www.w3.org/2000/svg">
      <defs>
        <linearGradient id="swooshFill" x1="0" y1="0" x2="1" y2="1">
          <stop offset="0" stop-color="var(--swoosh-grey)"/>
          <stop offset="0.45" stop-color="var(--swoosh-white)"/>
          <stop offset="1" stop-color="var(--swoosh-grey)"/>
        </linearGradient>
        <linearGradient id="bandFill" x1="0" y1="0" x2="0" y2="1">
          <stop offset="0" stop-color="var(--green-bright)"/>
          <stop offset="0.35" stop-color="var(--green-main)"/>
          <stop offset="1" stop-color="var(--green-deep)"/>
        </linearGradient>
        <linearGradient id="cornerFill" x1="0" y1="0" x2="1" y2="1">
          <stop offset="0" stop-color="var(--green-bright)"/>
          <stop offset="1" stop-color="var(--green-main)"/>
        </linearGradient>
      </defs>

      <!-- base green -->
      <rect class="base" width="1100" height="500" fill="var(--green-main)"/>

      <!-- light swoosh band -->
      <path class="swoosh" fill="url(#swooshFill)"
            d="M0 110 Q60 20 160 0 L730 0 Q960 150 1040 500 L800 500 Q380 360 0 300 Z"/>

      <!-- top-left green corner -->
      <path class="corner" fill="url(#cornerFill)"
            d="M0 0 L150 0 Q50 40 0 150 Z"/>

      <!-- bottom-left green band -->
      <path class="band" fill="url(#bandFill)"
            d="M0 300 Q380 330 800 500 L0 500 Z"/>

      <!-- feature photo frames -->
      <g role="img" aria-label="Photo: golf ball on a tee on the green">
        <ellipse cx="95" cy="215" rx="88" ry="80" fill="#5e9a3c"/>
        <ellipse class="feature-ring" cx="95" cy="215" rx="88" ry="80"/>
      </g>
      <g role="img" aria-label="Photo: wooden bridge over a lake with trees">
        <ellipse cx="305" cy="175" rx="112" ry="102" fill="#4f6f4a"/>
        <ellipse class="feature-ring" cx="305" cy="175" rx="112" ry="102"/>
      </g>
      <g role="img" aria-label="Photo: children on the jumping pillow">
        <ellipse cx="545" cy="170" rx="105" ry="98" fill="#8fa6b6"/>
        <ellipse class="feature-ring" cx="545" cy="170" rx="105" ry="98"/>
      </g>
      <g role="img" aria-label="Photo: family riding a red pedal bike on the water">
        <ellipse cx="745" cy="265" rx="95" ry="90" fill="#a24a3e"/>
        <ellipse class="feature-ring" cx="745" cy="265" rx="95" ry="90"/>
      </g>
      <g role="img" aria-label="Photo: Swiss style village and mini golf course">
        <ellipse cx="910" cy="395" rx="92" ry="88" fill="#6b7a4a"/>
        <ellipse class="feature-ring" cx="910" cy="395" rx="92" ry="88"/>
      </g>

      <!-- brand -->
      <text class="brand-name" x="1075" y="90" text-anchor="end">LOGO</text>
      <text class="brand-url" x="1075" y="122" text-anchor="end">www.brookmerefields.com</text>

      <!-- tagline -->
      <text class="tagline" x="80" y="385" font-size="46">
        <tspan class="strong">10 MINUTES</tspan><tspan class="light"> DRIVE</tspan>
      </text>
      <text class="tagline" x="80" y="440" font-size="46">
        <tspan class="light">NORTH OF </tspan><tspan class="strong">LAUNCESTON</tspan>
      </text>
    </svg>
  </div>
</div>
</body>
</html>
```